Specialist and reputable therapy practice needs a brochure design

We need an attractive brochure to market our specialist psychological therapy service called the "VEL Clinic" that helps women who are pregnant or with young babies experiencing mental health difficulties such as depression and anxiety. VEL Clinic is owned by Taleburn, a clinical psychology practice in Sydney Australia. We would like to have a 4 page glossy A4 or A5 brochure designed that uses our current logo. Note that we are needing the logo to be "sharpened" as text is difficult to read. Primary colours should include blue, lime green and pink that is consistent with our website (www.velclinic-example.com.au).

```html
<!DOCTYPE html>
<html lang="en">
<head>
<meta charset="utf-8">
<title>Introduction to the VEL Clinic</title>
<link rel="stylesheet" href="https://fonts.googleapis.com/css2?family=Arimo:wght@400;700&family=Roboto:wght@300&display=swap">
<style>
  :root {
    --pink-band: #f7bcd9;
    --magenta: #e5007e;
    --blue: #1ba1e2;
    --lime: #8cc63f;
    --ink: #2e2e2e;
    --white: #ffffff;
    --photo-warm: #d9c3a6;
    --photo-soft: #f1e6d2;
  }
  * { box-sizing: border-box; margin: 0; padding: 0; }
  html, body { width: 847px; height: 1200px; overflow: hidden; background: var(--white); }
  body { position: relative; font-family: "Arimo", Arial, sans-serif; color: var(--ink); }

  .title-band {
    position: absolute; left: 29px; top: 26px; width: 778px; height: 240px;
    background: var(--pink-band);
  }
  .title-band .kicker {
    position: absolute; left: 75px; top: 66px;
    font-family: "Roboto", Arial, sans-serif;
    font-weight: 300; font-size: 54px; line-height: 1; color: var(--white); letter-spacing: -0.8px;
  }
  .title-band .name {
    position: absolute; left: 71px; top: 122px;
    font-family: "Roboto", Arial, sans-serif;
    font-weight: 300; font-size: 98px; line-height: 1; color: var(--magenta); letter-spacing: -1.5px;
  }

  .side-bar { position: absolute; left: 0; top: 266px; width: 29px; height: 455px; background: var(--blue); }

  .hero-photo {
    position: absolute; left: 29px; top: 266px; width: 778px; height: 455px;
    background: linear-gradient(100deg, #8a7760 0%, var(--photo-soft) 35%, #e9d9c3 55%, var(--photo-warm) 80%, #6f604e 100%);
  }

  .columns { position: absolute; top: 750px; left: 41px; }
  .col {
    position: absolute; top: 0; width: 250px;
    font-size: 13.2px; line-height: 20.6px; color: var(--ink);
  }
  .col-intro { left: 0; }
  .col-symptoms { left: 266px; width: 262px; }
  .col-referral { left: 530px; width: 240px; }
  .col a { color: var(--magenta); text-decoration: none; }
  .col h2 { font-size: 16.5px; font-weight: 700; color: var(--blue); line-height: 21px; margin-bottom: 1px; }
  .col p + p { margin-top: 20.6px; }

  .page-footer {
    position: absolute; left: 28px; top: 1157px;
    display: flex; align-items: center; gap: 14px;
    font-size: 11px; font-weight: 700; color: var(--ink);
  }
  .page-footer .mark { width: 22px; height: 22px; border-radius: 50%; background: var(--lime); }
  .page-footer .num { color: var(--magenta); }
</style>
</head>
<body>
  <header class="title-band">
    <div class="kicker">Introduction to the</div>
    <h1 class="name">VEL Clinic</h1>
  </header>

  <div class="side-bar"></div>
  <div class="hero-photo" role="img" aria-label="Photo of two smiling women talking on a sofa, one holding a newborn baby"></div>

  <main class="columns">
    <section class="col col-intro">
      <p>Welcome to the Vital Early Life (VEL) Clinic. We are a specialist group of clinical psychologists that provide assessment and therapy services to mums and families struggling emotionally in the antenatal and postnatal period. We also provide support to women and couples who may have experienced trauma in this period of time, and those who may be struggling emotionally whilst trying to become pregnant. The Vital Early Life (VEL) Clinic is affiliated with <a href="#">Taleburn Clinical Psychologists</a> that provides clinical psychology services for other clinical problems experienced by adults, children and teenagers.</p>
    </section>

    <section class="col col-symptoms">
      <p>Perinatal depression and/or anxiety are accompanied by a range of symptoms that women find overwhelming, and can include: lowered mood; tearfulness; feelings of worthlessness; guilt and irritability; self-blame; anxiety and sometimes panic attacks; worries about the health of their baby; lack of energy and feelings of exhaustion; loss of interest in activities; sleep disturbance (not being able to sleep even when the baby is sleeping); reduced concentration and difficulty making decisions; feelings of hopelessness and inadequacy; and in some extreme cases thoughts about suicide and/or harming their baby. If you, or someone that you know, is affected by these symptoms, please make contact with our clinic for support.</p>
    </section>

    <section class="col col-referral">
      <h2>Referral Process</h2>
      <p>Women and families can initiate their own referral to the VEL Clinic or can be formally referred by a medical specialist.</p>
      <p>The Clinical Psychologists at the VEL Clinic are registered as specialists under Carecover and can therefore see clients for up to 10 appointments per calendar year under a Carecover Mental Health Care Plan (MHCP) issued by a GP or psychiatrist. Fees do occur a gap fee and sessions are charged slightly below the fee recommended by the Australian Psychology Guild.</p>
    </section>
  </main>

  <footer class="page-footer">
    <span class="mark"></span>
    <span>VEL Clinic | <span class="num">1</span></span>
  </footer>
</body>
</html>
```